Paws About Town Helpers

Design a flyer (A5 - I think!) with bright colours to promote an in home Dog Service.
Include an animated picture of a dog (being walked/playing/jumping etc)
Bold Heading, list of services with animated pictures, contact details

Industry/Entity Type

It Service

Requirements
Must have
• Add price list to back of A5 Flyer with same colours and design as front page of flyer - See Attached.

```html
<!DOCTYPE html>
<html lang="en">
<head>
<meta charset="utf-8">
<title>Paws About Town Helpers – Dog Services Flyer</title>
<link rel="stylesheet" href="https://fonts.googleapis.com/css2?family=Comfortaa:wght@700&family=Arimo:ital,wght@0,700;1,700&display=swap">
<style>
  :root {
    --paper: #ffffff;
    --ink: #111111;
    --paw: #f8c6ad;
    --band-green: #00a651;
    --band-yellow: #fff200;
    --band-orange: #f7941d;
    --band-red: #ed1c24;
    --band-magenta: #ec008c;
    --band-purple: #662d91;
    --band-blue: #2e3192;
    --band-cyan: #00aeef;
    --banner-light: #fff7b0;
    --banner-deep: #ffdc00;
    --service-text: #ffffff;
    --photo-cream: #d9cdb8;
    --photo-fawn: #a8977c;
    --photo-dark: #4a3a2c;
  }
  * { margin: 0; padding: 0; box-sizing: border-box; }
  html, body { width: 849px; height: 1200px; overflow: hidden; background: var(--paper); }
  .flyer { position: relative; width: 849px; height: 1200px; overflow: hidden; background: var(--paper); }

  .paw-artwork {
    position: absolute; left: 57px; top: 165px; width: 736px; height: 892px;
    border-radius: 110px;
    background: var(--paw);
  }

  .headline {
    position: absolute; left: 0; top: 24px; width: 849px;
    text-align: center; color: var(--ink);
    font-family: "Comfortaa", sans-serif; font-weight: 700;
    text-shadow: 0 6px 10px rgba(0,0,0,0.35);
  }
  .headline__intro { display: block; font-size: 52px; line-height: 58px; }
  .headline__name { display: block; font-size: 50px; line-height: 60px; letter-spacing: 0.5px; }

  .dog-photo {
    position: absolute; left: 340px; top: 145px; width: 230px; height: 360px;
    border-radius: 40px;
    background: radial-gradient(ellipse 60% 55% at 50% 50%, var(--photo-cream) 0%, var(--photo-fawn) 60%, var(--photo-dark) 100%);
  }

  .services-band {
    position: absolute; left: 0; top: 520px; width: 849px; height: 315px;
    background: linear-gradient(to bottom,
      var(--band-green) 0%, var(--band-yellow) 14%, var(--band-orange) 30%,
      var(--band-red) 44%, var(--band-magenta) 58%, var(--band-purple) 72%,
      var(--band-blue) 84%, var(--band-cyan) 100%);
    padding-top: 15px;
    text-align: center; color: var(--service-text);
    font-family: "Arimo", Arial, sans-serif; font-weight: 700; font-style: italic;
    font-size: 22.5px; line-height: 28px; white-space: nowrap;
    text-shadow: 0 2px 5px rgba(0,0,0,0.55);
  }
  .service__question, .service__answer { display: block; }

  .contact-banner {
    position: absolute; left: 62px; top: 910px; width: 740px; height: 236px;
    background: linear-gradient(to right, var(--banner-light), var(--banner-deep));
  }
  .contact {
    position: absolute; left: 178px; top: 958px;
    font-family: "Arimo", Arial, sans-serif; font-weight: 700; font-style: normal;
    font-size: 17px; line-height: 24px; color: var(--ink);
  }
  .contact__details { margin-top: 26px; }
</style>
</head>
<body>
<main class="flyer">
  <div class="paw-artwork" role="img" aria-label="Large peach paw print illustration behind the content"></div>

  <h1 class="headline">
    <span class="headline__intro">WE ARE:</span>
    <span class="headline__name">Paws About Town Helpers</span>
  </h1>

  <div class="dog-photo" role="img" aria-label="Photo of a fawn pug puppy standing"></div>

  <section class="services-band">
    <span class="service__question">TIRED OF PICKING UP DOG POOP?</span>
    <span class="service__answer">- arrange for us to do it for you!</span>
    <span class="service__question">NEED A BREAK FROM WALKING THE DOG?</span>
    <span class="service__answer">- we will come and collect your dog and take it for a walk!</span>
    <span class="service__question">CAN’T GET HOME IN TIME TO FEED YOUR DOG?</span>
    <span class="service__answer">- use our dog feeding service!</span>
    <span class="service__question">WANT SOMEONE TO PLAY WITH YOUR DOG WHILE YOU’RE AT WORK?</span>
    <span class="service__answer">- we will be Paws About Town Helpers!</span>
    <span class="service__question">DOG NEEDS A BATH?</span>
    <span class="service__answer">- we’ll arrange for a professional to keep it clean!</span>
  </section>

  <div class="contact-banner" role="img" aria-label="Yellow ribbon banner behind the contact details"></div>

  <address class="contact">
    <p>FOR ALL SERVICES RELATED TO YOUR DOG – CALL PATH<br>“Paws About Town Helpers”</p>
    <p class="contact__details">Tel: 0400 318 527<br>Web: www.pawsabouttownhelpers.com.au</p>
  </address>
</main>
</body>
</html>
```